CalmPath Nurses' Manifesto

Design a manifesto to inspire and motivate nurses to work at minimum standards of excellence in their nursing practice.

The manifesto will become a feature of our website, at conferences, workshops and retreats. It will also be featured on other marketing tools.

Primary Market:
Nurses and/or other healthcare professionals (specifically Doctors, Occupational Therapists, Psychologists and Social Workers).

However the manifesto is equally applicable to all nurses and healthcare professionals from new graduates to very experienced senior clinicians, administration officers,managers and healthcare executive personnel.

Mainly females and primarily 35 to 65 years old, which suggests people in this target age group have extensive experience, but have become jaded'.

The purpose of our business is to assist healthcare professionals, primarily nurses, to maintain their enthusiasm and excellence in service provision, for their benefit as well as the benefit of the clients.

I have attached:
File 1: Copy Samples and examples: which has the copy for the manifesto, examples that appeal to us and our 3 attempts.
File 2: Our colour Spec Sheet, HOWEVER the colours are not necessary limited to these colours. These colours are not in the logo that will be on the manifesto. The colours on the logo attached can/or also be used.
File 3: Prototype logo. The final logo will be available within 3 to 4 days.

Requirements
Must have
• Must use the copy as per the attached file.

It should be contemporary, eye catching and motivational.

Sample 1 on the attached file (File 3: copy, samples and examples_554207 saturday, 29 june 2013 06:24:3030) Is close to what we are looking for.
Should not have
• MUST BE EASY TO READ. Each line MUST be clearly defined from each other.

```html
<!DOCTYPE html>
<html lang="en">
<head>
<meta charset="utf-8">
<title>CalmPath Nurses' Manifesto</title>
<link rel="stylesheet" href="https://fonts.googleapis.com/css2?family=Oswald:wght@200;300;400;600;700&family=Fredoka:wght@600&family=Roboto+Slab:wght@800&family=Arimo:wght@400;700&family=Sanchez&family=Josefin+Sans:wght@700&family=Josefin+Slab:wght@600&family=Gilda+Display&display=swap">
<style>
  :root {
    --orange: #f05a28;
    --teal: #1e5f63;
    --cyan: #2fb5c7;
    --green: #8dc63f;
    --mint: #4fbfa8;
    --paper: #ffffff;
  }
  * { margin: 0; padding: 0; box-sizing: border-box; }
  html, body { width: 792px; height: 1200px; overflow: hidden; background: var(--paper); }
  .poster { position: relative; width: 792px; height: 1200px; overflow: hidden; background: var(--paper); }
  .poster > * { position: absolute; white-space: nowrap; }

  .rule-dots { height: 3px; background-image: radial-gradient(circle, currentColor 1.2px, transparent 1.4px); background-size: 6px 3px; }
  .rule-solid { height: 2px; background: currentColor; }
  .rule-hatch { height: 6px; background: repeating-linear-gradient(135deg, currentColor 0 1.5px, transparent 1.5px 3.5px); }

  .hatched {
    font-family: "Fredoka", sans-serif; font-weight: 600;
    color: transparent;
    background: repeating-linear-gradient(135deg, var(--ink) 0 1.4px, transparent 1.4px 3.6px);
    -webkit-background-clip: text; background-clip: text;
    -webkit-text-stroke: 1.5px var(--ink);
    text-transform: uppercase; line-height: 1;
    transform-origin: top left;
  }

  .title { left: 30px; top: 58px; font-family: "Oswald", sans-serif; font-weight: 400; font-size: 88px; line-height: 1; letter-spacing: 4px; color: var(--orange); transform: scaleY(1.12); transform-origin: top left; }
  .open-hands { left: 30px; top: 174px; --ink: var(--cyan); font-size: 38px; line-height: 37px; transform: scaleY(1.35); }
  .self-care { left: 358px; top: 174px; font-family: "Arimo", sans-serif; font-size: 16px; line-height: 1.4; color: var(--teal); font-weight: 400; }
  .self-care b { font-weight: 700; }
  .delight { left: 357px; top: 226px; font-family: "Oswald", sans-serif; font-weight: 600; font-size: 26px; line-height: 1.18; color: var(--green); }
  .support { left: 30px; top: 331px; font-family: "Oswald", sans-serif; font-weight: 300; font-size: 27px; line-height: 1.1; letter-spacing: 1.2px; color: var(--orange); }
  .respect { left: 426px; top: 304px; font-family: "Roboto Slab", serif; font-weight: 800; font-size: 56px; letter-spacing: 11px; line-height: 1; color: var(--teal); }
  .respect-note { left: 426px; top: 364px; font-family: "Arimo", sans-serif; font-weight: 700; font-size: 16px; line-height: 1.3; color: var(--teal); }
  .learn-daily { left: 30px; top: 414px; --ink: var(--mint); font-size: 41px; letter-spacing: 1.2px; }
  .trust { left: 30px; top: 462px; font-family: "Sanchez", serif; font-size: 21px; letter-spacing: 1.1px; color: var(--green); }
  .lifelong { left: 30px; top: 498px; font-family: "Oswald", sans-serif; font-weight: 600; color: var(--teal); line-height: 1; }
  .lifelong .small { display: block; font-size: 42px; }
  .lifelong .big { display: block; font-size: 66px; margin-top: 0; }
  .diversity { left: 292px; top: 512px; font-family: "Oswald", sans-serif; font-weight: 300; font-size: 32px; line-height: 1.18; letter-spacing: 1.5px; color: var(--teal); }
  .smile { left: 30px; top: 602px; font-family: "Sanchez", serif; font-size: 23px; letter-spacing: 0.8px; color: var(--green); }
  .right-thing { left: 30px; top: 652px; font-family: "Josefin Sans", sans-serif; font-weight: 700; color: var(--green); line-height: 1.12; text-transform: uppercase; }
  .right-thing .l1 { display: block; font-size: 42px; }
  .right-thing .l2 { display: block; font-size: 29px; }
  .right-thing .l3 { display: block; font-size: 24px; }
  .unique { left: 332px; top: 652px; --ink: var(--cyan); font-size: 36px; line-height: 1.1; letter-spacing: 0.4px; }
  .within { left: 333px; top: 736px; font-family: "Oswald", sans-serif; font-weight: 300; font-size: 22px; letter-spacing: 3.4px; color: var(--orange); }
  .solution { left: 28px; top: 766px; font-family: "Oswald", sans-serif; font-weight: 200; font-size: 54px; letter-spacing: 4.5px; line-height: 1; color: var(--cyan); transform: scaleY(1.12); transform-origin: top left; }
  .leaders { left: 30px; top: 843px; font-family: "Oswald", sans-serif; font-weight: 600; font-size: 30px; color: var(--green); line-height: 1; }
  .lead-purpose { left: 30px; top: 896px; font-family: "Arimo", sans-serif; font-weight: 700; font-size: 14.5px; color: var(--orange); letter-spacing: 0.4px; }
  .respond { left: 30px; top: 936px; font-family: "Josefin Slab", serif; font-weight: 600; font-size: 23px; line-height: 1.2; color: var(--teal); }
  .choose { left: 30px; top: 1038px; font-family: "Josefin Sans", sans-serif; font-weight: 700; font-size: 19.5px; line-height: 1.45; color: var(--teal); }
  .choose b { font-size: 22px; }
  .dream { left: 30px; top: 1080px; font-family: "Oswald", sans-serif; font-weight: 600; color: var(--teal); line-height: 1; }
  .dream .live { font-size: 48px; }
  .dream .word { font-size: 84px; }
  .follow { left: 495px; top: 846px; font-family: "Gilda Display", serif; font-size: 26px; line-height: 1.25; color: var(--teal); }
  .lead { left: 497px; top: 912px; --ink: var(--teal); font-size: 96px; letter-spacing: 0; transform: scaleY(1.1); }
  .can-do { left: 495px; top: 1026px; font-family: "Oswald", sans-serif; font-weight: 200; font-size: 20px; line-height: 1.6; letter-spacing: 2.5px; color: var(--teal); }
  .brand { left: 652px; top: 1118px; display: flex; align-items: center; gap: 6px; font-family: "Oswald", sans-serif; font-weight: 400; font-size: 17px; color: var(--teal); }
  .brand .dot { width: 14px; height: 14px; border-radius: 50%; background: var(--cyan); }
</style>
</head>
<body>
<main class="poster">
  <div class="rule-dots" style="left:30px;top:38px;width:735px;color:var(--cyan)"></div>
  <div class="rule-solid" style="left:30px;top:46px;width:735px;color:var(--teal)"></div>
  <div class="rule-solid" style="left:30px;top:50px;width:735px;color:var(--cyan)"></div>
  <h1 class="title">NURSES' MANIFESTO</h1>
  <div class="rule-solid" style="left:30px;top:150px;width:735px;color:var(--teal)"></div>
  <div class="rule-solid" style="left:30px;top:154px;width:735px;color:var(--cyan)"></div>
  <div class="rule-dots" style="left:30px;top:161px;width:735px;color:var(--cyan)"></div>

  <p class="hatched open-hands">Nurse with<br>Open hands,<br>Hearts &amp; minds</p>
  <p class="self-care">Look after <b>YOURSELF &amp; VALUE YOUR HEALTH</b><br>as much as you value the <b>HEALTH OF OTHERS</b></p>
  <p class="delight">DELIGHT YOUR CLIENTS &amp; COLLEAGUES<br>BY EXCEEDING THEIR EXPECTATIONS</p>

  <div class="rule-hatch" style="left:30px;top:320px;width:378px;color:var(--orange)"></div>
  <p class="support">SUPPORT YOUR COLLEAGUES AND<br>CHAMPION THEIR PURPOSE.</p>
  <div class="rule-hatch" style="left:30px;top:397px;width:378px;color:var(--orange)"></div>
  <p class="respect">RESPECT</p>
  <p class="respect-note">the limits of people's KNOWLEDGE &amp;<br>SHARE YOUR knowledge generously.</p>

  <p class="hatched learn-daily">Learn something new each day</p>
  <p class="trust">Trust your knowledge &amp; seek advice only from respected sources.</p>

  <div class="rule-hatch" style="left:292px;top:503px;width:473px;color:var(--teal)"></div>
  <p class="lifelong"><span class="small">BE A LIFELONG</span><span class="big">LEARNER</span></p>
  <p class="diversity">CELEBRATE, RESPECT AND VALUE THE<br>DIVERSITY OF AUSTRALIAN CULTURE.</p>
  <div class="rule-hatch" style="left:292px;top:589px;width:473px;color:var(--teal)"></div>

  <p class="smile">SMILE &amp; INFECT others with your HAPPINESS &amp; have FUN!</p>

  <div class="rule-solid" style="left:30px;top:640px;width:285px;color:var(--green)"></div>
  <div class="rule-solid" style="left:30px;top:644px;width:285px;color:var(--green)"></div>
  <div class="rule-dots" style="left:332px;top:641px;width:433px;color:var(--cyan)"></div>
  <p class="right-thing"><span class="l1">Always do</span><span class="l2">the RIGHT thing</span><span class="l3">with out exception</span></p>
  <p class="hatched unique">You are unique, revel<br>in your individuality.</p>
  <p class="within">SEEK SUCCESS FIRSTLY FROM WITHIN.</p>

  <p class="solution">ALWAYS BE SOLUTION FOCUSED</p>

  <div class="rule-dots" style="left:30px;top:832px;width:450px;color:var(--green)"></div>
  <p class="leaders">ONLY FOLLOW EXCEPTIONAL LEADERS.</p>
  <div class="rule-dots" style="left:30px;top:883px;width:450px;color:var(--orange)"></div>
  <p class="lead-purpose">ALWAYS LEAD WITH PURPOSE, PASSION &amp; COMMITMENT.</p>
  <div class="rule-dots" style="left:30px;top:922px;width:450px;color:var(--orange)"></div>
  <p class="respond">“RESPOND to complex situations<br>INNOVATIVELY, CREATIVELY &amp; SAFELY<br>within the scope of your practice.”</p>

  <div class="rule-solid" style="left:30px;top:1028px;width:450px;color:var(--green)"></div>
  <div class="rule-solid" style="left:30px;top:1032px;width:450px;color:var(--cyan)"></div>
  <p class="choose"><b>CHOOSE</b> your thoughts wisely, they create<br><b>YOUR REALITY.</b></p>
  <div class="rule-dots" style="left:270px;top:1077px;width:210px;color:var(--teal)"></div>
  <p class="dream"><span class="live">LIVE YOUR </span><span class="word">DREAM</span></p>
  <div class="rule-dots" style="left:30px;top:1160px;width:450px;color:var(--teal)"></div>

  <div class="rule-hatch" style="left:495px;top:832px;width:270px;color:var(--teal)"></div>
  <p class="follow">IF THERE IS NO ONE<br>left to follow, then</p>
  <p class="hatched lead">Lead!</p>
  <div class="rule-hatch" style="left:495px;top:1013px;width:270px;color:var(--teal)"></div>
  <p class="can-do">ADOPT A ‘CAN DO’ ATTITUDE<br>TO EVERYTHING THAT COMES<br>YOUR WAY.</p>

  <div class="brand"><span class="dot"></span><span>CalmPath</span></div>
</main>
</body>
</html>
```